Surgical Procedure Room Letterhead

PLEASE DO NOT MAKE YOUR LETTERHEAD SIMILAR TO THE ONE I AM INCLUDING IN MY UPLOADS

Hello! I need my logo used to make a very clean, professional, simple letterhead that has all the pertinent information in it:
Location: 4182 NW 38th Lane, Suite 500
Tamarac, FL 33967
Phone: 954-218-4650
Fax: 800-642-9082

Can you please put this all on a word document that is easily editable? I will include my practice letterhead as an example ONLY of how easy it should be to write below the letterhead. Please don't make this letterhead the same as the one I am including in this example. They are two separate businesses.

Target Market(s)

Insurance companies

Industry/Entity Type

medical

Requirements
Must have
• classiness, elegance, simplicity
Should not have
• Please don't make your letterhead the same as the one that I included in my uploads

```html
<!DOCTYPE html>
<html lang="en">
<head>
<meta charset="utf-8">
<title>Meridian Care Suites — Letterhead</title>
<link rel="stylesheet" href="https://fonts.googleapis.com/css2?family=PT+Serif&family=Source+Sans+3:wght@400&display=swap">
<style>
  :root {
    --backdrop: #dedede;
    --paper: #f7f7f7;
    --navy: #13294f;
    --gold: #d9b548;
    --body-text: #5a5a5a;
    --footer-text: #555555;
  }
  * { box-sizing: border-box; margin: 0; padding: 0; }
  html, body {
    width: 1153px; height: 1200px; overflow: hidden;
    background: var(--backdrop);
  }
  .letterhead {
    position: absolute; left: 145px; top: 0;
    width: 862px; height: 1200px;
    background: var(--paper);
  }
  .brand {
    position: absolute; top: 82px; left: 0; width: 100%;
    display: flex; align-items: center; justify-content: center;
  }
  .brand-name {
    font-family: "PT Serif", serif; font-size: 34px; line-height: 1.05;
    color: var(--navy); letter-spacing: 0.5px; text-align: center;
  }
  .letter-body {
    position: absolute; left: 85px; top: 268px; width: 691px;
    font-family: "Source Sans 3", sans-serif; font-size: 15.3px;
    line-height: 22.6px; color: var(--body-text);
  }
  .letter-body p { margin-bottom: 22.6px; text-align: justify; }
  .letter-body .salutation, .letter-body .closing { text-align: left; }
  .signature {
    position: absolute; left: 85px; top: 864px; width: 100px; height: 94px;
    background: linear-gradient(135deg, rgba(19,41,79,0.18), rgba(19,41,79,0.06));
    border-radius: 4px;
  }
  .footer-rule {
    position: absolute; left: 85px; top: 1092px; width: 691px; height: 0;
    border-top: 1.5px solid var(--gold);
  }
  .contact {
    position: absolute; left: 0; top: 1114px; width: 100%;
    font-family: "PT Serif", serif; font-size: 17px; line-height: 25px;
    color: var(--footer-text); text-align: center;
  }
  .contact-line { display: flex; justify-content: center; align-items: center; gap: 7px; }
  .contact-line svg { fill: var(--navy); }
  .contact-line .gap { width: 4px; }
</style>
</head>
<body>
  <main class="letterhead">
    <header class="brand">
      <span class="brand-name">Meridian<br>Care Suites</span>
    </header>

    <section class="letter-body">
      <p class="salutation">Dear customer,</p>
      <p>Lorem ipsum dolor sit amet, consectetur adipisicing elit, sed do eiusmod tempor incididunt ut labore et dolore magna aliqua. Ut enim ad minim veniam, quis nostrud exercitation ullamco laboris nisi ut aliquip ex ea commodo consequat. Duis aute irure dolor in reprehenderit in voluptate velit esse cillum dolore eu fugiat nulla pariatur. Excepteur sint occaecat cupidatat non proident, sunt in culpa qui officia deserunt mollit anim id est laborum.</p>
      <p>Lorem ipsum dolor sit amet, consectetur adipisicing elit, sed do eiusmod tempor incididunt ut labore et dolore magna aliqua. Ut enim ad minim veniam, quis nostrud exercitation ullamco laboris nisi ut aliquip ex ea commodo consequat. Duis aute irure dolor in reprehenderit in voluptate velit esse cillum dolore eu fugiat nulla pariatur. Excepteur sint occaecat cupidatat non proident, sunt in culpa qui officia deserunt mollit anim id est laborum.</p>
      <p>Lorem ipsum dolor sit amet, consectetur adipisicing elit, sed do eiusmod tempor incididunt ut labore et dolore magna aliqua. Ut enim ad minim veniam, quis nostrud exercitation ullamco laboris nisi ut aliquip ex ea commodo consequat. Duis aute irure dolor in reprehenderit in voluptate velit esse cillum dolore eu fugiat nulla pariatur. Excepteur sint occaecat cupidatat non proident, sunt in culpa qui officia deserunt mollit anim id est laborum.</p>
      <p>Lorem ipsum dolor sit amet, consectetur adipisicing elit, sed do eiusmod tempor incididunt ut labore et dolore magna aliqua. Ut enim ad minim veniam, quis nostrud exercitation ullamco laboris nisi ut aliquip ex ea commodo consequat. Duis aute irure dolor in reprehenderit.</p>
      <p class="closing">Yours Sincerely,</p>
    </section>

    <div class="signature" role="img" aria-label="Handwritten signature"></div>

    <div class="footer-rule"></div>

    <footer class="contact">
      <div class="contact-line">
        <svg width="17" height="15" viewBox="0 0 17 15" aria-hidden="true"><path d="M1 5c0-3 4-4 7.5-4S16 2 16 5l-3 1-1-2H5L4 6z"/><path d="M5 6h7l3 5v3H2v-3zm3.5 2a2 2 0 1 0 0 4 2 2 0 0 0 0-4z"/></svg>
        <span>954-218-4650</span>
        <span class="gap"></span>
        <svg width="19" height="15" viewBox="0 0 19 15" aria-hidden="true"><path d="M5 0h9v5H5z"/><path d="M1 6h17v9H1zm3 2v2h11V8z" fill-rule="evenodd"/></svg>
        <span>800-642-9082</span>
      </div>
      <div>4182 NW 38th Lane, Suite 500 Tamarac, FL 33967</div>
    </footer>
  </main>
</body>
</html>
```